Copper Lantern LLC Business Card

We need a business card design for a newco in Texas. We are a team of professionals who join start ups as founders and help launch their businesses, which are primarily related to food and beverage and the service side of the industry. We love local and craft and are partners in businesses in the local meat, BBQ and Burger, fine dining, and beverage alcohol businesses. Our specialty is finance and the business side of start ups, including assisting with capital raises as principals, not brokers. We do not currently have any logos or graphics for this entity. Our values include helping people succeed, rooting for the underdog, healthy food, the environment and being good citizens.

Target Market(s)

Everybody but also Angel Investors, CPAs, Bankers, Entrepreneurs

Industry/Entity Type

Business

Contact Information for Business Card

Fields for Business Name, Title, Email Address, Phone Number. Place to add mailing address and web domain later.

Font styles to use
Sans Serif

Colors

Designer to choose colors to be used in the design.

Requirements
Should not have
• Pictures of booze bottles or drinks thought there could be a social scene that does not strictly focus on those. No cows, cowboy hats or ranches. We are not a Wall Street type entity so no huge office buildings or skylines.

```html
<!DOCTYPE html>
<html lang="en">
<head>
<meta charset="utf-8">
<title>Business Card</title>
<link rel="stylesheet" href="https://fonts.googleapis.com/css2?family=Arimo:wght@400;700&display=swap">
<style>
  :root {
    --paper: #ffffff;
    --red: #ec2427;
    --charcoal: #2a2a2a;
    --slate: #555555;
    --ink: #262626;
    --ink-soft: #333333;
    --grey-text: #8c8c8c;
    --dots: #d9d9d9;
    --swirl-warm: #f7dc9a;
    --swirl-cool: #cfe7d9;
  }
  * { box-sizing: border-box; }
  html, body {
    margin: 0;
    width: 1200px;
    height: 586px;
    overflow: hidden;
    background: var(--paper);
  }
  .card {
    position: relative;
    width: 1200px;
    height: 586px;
    background: var(--paper);
    border: 1px solid #222;
    font-family: "Arimo", Arial, sans-serif;
    overflow: hidden;
  }
  .card__art {
    position: absolute;
    inset: 0;
  }
  .swirl-backdrop {
    position: absolute;
    left: 0;
    top: 0;
    width: 760px;
    height: 586px;
    background:
      radial-gradient(ellipse 330px 280px at 330px 250px, rgba(255,255,255,1) 55%, rgba(255,255,255,0) 72%),
      radial-gradient(ellipse 420px 330px at 330px 260px, var(--swirl-warm) 0%, rgba(247,220,154,0.35) 60%, rgba(255,255,255,0) 100%),
      linear-gradient(160deg, rgba(255,255,255,0) 40%, var(--swirl-cool) 85%, rgba(255,255,255,0) 100%);
    opacity: 0.55;
  }
  .company {
    position: absolute;
    left: 86px;
    top: 142px;
    margin: 0;
    font-size: 58px;
    font-weight: 700;
    letter-spacing: -0.5px;
    line-height: 1;
    color: var(--ink-soft);
  }
  .company__lead { color: var(--ink); }
  .tagline {
    position: absolute;
    left: 175px;
    top: 209px;
    margin: 0;
    font-size: 20px;
    font-weight: 700;
    color: var(--grey-text);
  }
  .detail {
    position: absolute;
    display: flex;
    align-items: center;
    margin: 0;
    font-size: 20px;
    font-weight: 700;
    color: var(--grey-text);
  }
  .detail--web { left: 94px; top: 431px; }
  .detail--address { left: 94px; top: 523px; }
  .icon { position: absolute; }
  .name {
    position: absolute;
    left: 768px;
    top: 156px;
    margin: 0;
    font-size: 41px;
    font-weight: 700;
    color: var(--paper);
    letter-spacing: 0.5px;
  }
  .role {
    position: absolute;
    left: 908px;
    top: 240px;
    margin: 0;
    font-size: 28px;
    font-weight: 400;
    color: var(--paper);
  }
  .contact {
    position: absolute;
    left: 834px;
    margin: 0;
    font-size: 27px;
    color: var(--paper);
    letter-spacing: 0.3px;
  }
  .contact--phone { top: 363px; }
  .contact--email { top: 438px; }
</style>
</head>
<body>
<main class="card">
  <div class="swirl-backdrop" role="img" aria-label="Faint background of sweeping curved lines in soft orange, yellow and green"></div>

  <svg class="card__art" width="1200" height="586" viewBox="0 0 1200 586" aria-hidden="true">
    <polygon points="900,0 1200,0 1200,586 555,586" fill="var(--red)"/>
    <polygon points="664,226 768,226 736,277" fill="var(--slate)"/>
    <rect x="664" y="138" width="532" height="88" fill="var(--charcoal)"/>
    <line x1="785" y1="418" x2="1106" y2="418" stroke="var(--dots)" stroke-width="4" stroke-linecap="round" stroke-dasharray="0 8"/>

    <!-- phone icon -->
    <g class="icon-phone">
      <rect x="778" y="364" width="32" height="32" fill="var(--charcoal)"/>
      <rect x="787" y="369" width="14" height="22" rx="2" fill="none" stroke="var(--paper)" stroke-width="2"/>
    </g>
    <!-- email icon -->
    <g class="icon-email">
      <rect x="778" y="438" width="41" height="30" fill="var(--charcoal)"/>
      <rect x="785" y="445" width="27" height="17" fill="var(--paper)"/>
      <polyline points="785,445 798.5,455 812,445" fill="none" stroke="var(--charcoal)" stroke-width="1.5"/>
    </g>
    <!-- monitor icon -->
    <g class="icon-web">
      <rect x="13" y="403" width="71" height="47" rx="2" fill="var(--ink)"/>
      <rect x="17" y="407" width="63" height="37" fill="var(--paper)"/>
      <text x="48.5" y="431" text-anchor="middle" font-family="Arimo, Arial, sans-serif" font-size="13" font-weight="700" fill="var(--ink)">www.</text>
      <rect x="44" y="450" width="9" height="6" fill="var(--ink)"/>
      <rect x="34" y="456" width="29" height="3" fill="var(--ink)"/>
    </g>
    <!-- map pin icon -->
    <g class="icon-address" fill="none" stroke="var(--ink)" stroke-width="3" stroke-linejoin="round">
      <polygon points="20,548 30,518 44,524 58,518 76,524 78,548 62,542 46,548 32,542"/>
      <line x1="32" y1="520" x2="32" y2="542"/>
      <line x1="60" y1="519" x2="62" y2="542"/>
      <path d="M55,520 L46,510" />
      <path d="M46,530 C40,518 34,510 34,501 A12,12 0 0 1 58,501 C58,510 52,518 46,530 Z" fill="var(--paper)"/>
      <circle cx="46" cy="501" r="4"/>
    </g>
  </svg>

  <h1 class="company"><span class="company__lead">YOUR</span>COMPANY</h1>
  <p class="tagline">YOUR TAGLINE GOES HERE</p>
  <p class="detail detail--web">WWW.YOURWEBSITE.COM</p>
  <p class="detail detail--address">CITY ADDRESS HERE</p>

  <h2 class="name">YOUR NAME HERE</h2>
  <p class="role">MANAGER</p>
  <p class="contact contact--phone">+00 123 456 789</p>
  <p class="contact contact--email">your@email.com</p>
</main>
</body>
</html>
```